Tidewell Care Community Catalogue

I would like an A4 brochure designed consistent with my company branding . This can be seen at www.tidewellcare.com.au . All content is available in document below.

I've also included the brand guidelines document.

Target Market(s)

People in the community suffering from injuries & Disabilities

Industry/Entity Type

Health Service

Font styles to use

Colors
33b8a4
acd037

Requirements
Must have
• Good use of the pictures I've included.
• Brand colours & Fonts
• Consistency with brand look and feel

```html
<!DOCTYPE html>
<html lang="en">
<head>
<meta charset="utf-8">
<title>Tidewell Care Community Catalogue – Spread 4–5</title>
<link rel="stylesheet" href="https://fonts.googleapis.com/css2?family=Josefin+Sans:wght@300;400&family=Open+Sans:ital,wght@0,400;0,700;1,300&display=swap">
<style>
  :root{
    --bg:#d9dadb;
    --blue-top:#3a86c2;
    --blue-bottom:#5aa8d6;
    --page-light:#f4f5f6;
    --ink:#3a3f44;
    --white:#ffffff;
    --band-sky:#4a9fd3;
    --band-navy:#1f5f9c;
    --band-green:#3aa24a;
    --band-purple:#8b2e8f;
    --band-violet:#6a3a98;
    --band-grey:#8c8f93;
    --brand-purple:#7d4a9d;
  }
  *{box-sizing:border-box;margin:0;padding:0}
  html,body{width:1200px;height:857px;overflow:hidden;background:var(--bg)}
  .spread{position:absolute;left:60px;top:30px;width:1080px;height:797px;display:flex;box-shadow:0 8px 24px rgba(0,0,0,.18)}
  .page{position:relative;width:540px;height:797px;overflow:hidden;font-family:"Open Sans",sans-serif}
  .page--left{background:linear-gradient(160deg,var(--blue-top),var(--blue-bottom));color:var(--white)}
  .page--right{background:var(--page-light);color:var(--ink)}
  .guides{position:absolute;inset:0;width:100%;height:100%}
  .page-title{position:absolute;top:52px;left:0;right:0;text-align:center;font-family:"Josefin Sans",sans-serif;font-weight:300;font-size:24px;letter-spacing:1.5px}
  .photo{position:absolute;left:80px;top:100px;width:380px;height:240px;background:linear-gradient(135deg,#c9d3dc,#9fb0bf 55%,#6b4a5a);border:3px solid var(--white)}
  .pull-quote{position:absolute;left:70px;right:70px;top:362px;text-align:center;font-style:italic;font-weight:300;font-size:17px;line-height:1.3}
  .columns{position:absolute;top:430px;left:44px;right:44px;display:flex;gap:22px;font-size:7.4px;line-height:1.45}
  .columns p{margin-bottom:6px}
  .columns h3{font-size:7.6px;font-weight:700;margin:4px 0 3px}
  .col{flex:1}
  .brand-mark{position:absolute;left:50px;bottom:78px;font-family:"Open Sans",sans-serif;font-weight:700;font-size:16px;color:var(--white)}
  .folio{position:absolute;bottom:36px;font-family:"Josefin Sans",sans-serif;font-size:14px}
  .page--left .folio{left:240px}
  .page--right .folio{left:260px;color:var(--band-sky)}
  .bands{position:absolute;left:0;right:0;bottom:0;height:26px;display:flex}
  .bands span{flex:1}
  .b1{background:var(--band-sky)}.b2{background:var(--band-navy)}.b3{background:var(--band-green)}
  .b4{background:var(--band-purple)}.b5{background:var(--band-violet)}.b6{background:var(--band-grey)}
  .scheme-name{position:absolute;top:100px;left:0;right:0;text-align:center;font-family:"Open Sans",sans-serif;font-weight:700;font-size:38px;color:var(--brand-purple)}
  .page--right .page-title{color:var(--ink);font-size:22px}
  .page--right .columns{top:172px;color:var(--ink)}
</style>
</head>
<body>
<div class="spread">
  <section class="page page--left">
    <svg class="guides" viewBox="0 0 540 797" aria-hidden="true">
      <g stroke="rgba(255,255,255,.25)" stroke-width="1" fill="none">
        <line x1="270" y1="0" x2="60" y2="640"/>
        <line x1="540" y1="90" x2="140" y2="797"/>
        <line x1="0" y1="300" x2="540" y2="520"/>
      </g>
    </svg>
    <h1 class="page-title">THE ‘YOU’ IN ‘COMMUNITY’</h1>
    <div class="photo" role="img" aria-label="Photo: a physiotherapist guiding an older woman through a stretching exercise on a mat in a bright clinic gym"></div>
    <p class="pull-quote">It’s no coincidence that the word ‘community’ contains the letters ‘y’, ‘o’ and ‘u’.</p>
    <div class="columns">
      <div class="col">
        <p>Tidewell Care’s unique emphasis on community is founded on a commitment to help individuals of all ages to realise their personal best health and wellbeing, no matter what their injuries, disabilities or limitations. To us, the word community means harnessing your personal strengths to enable your participation in a rich, rewarding, connected life. It means person-centred services and community engagement processes tailored to ensuring that clients with special needs receive the care they require and deserve, to realise their potential and enjoy optimal quality of life. It means a collaborative approach to treatment and partnering you on your journey. Tidewell Care’s community practitioners will support you to challenge your limitations and celebrate your progress as you gain confidence and accomplish things you didn’t believe you could.</p>
        <h3>What sets us apart</h3>
      </div>
      <div class="col">
        <p>Since initially gaining national acclaim for helping athletes to reach their peak performance, Tidewell Care has earned a reputation for its unique, dedicated community focus. Led by director and senior chiropractor Dr Lena Ortiz, who is passionate about each person’s right to know what it is to feel well and live their best life, our practice has become widely known among health practitioners and case managers as a caring, compassionate, specialised private practice with dedicated services and knowledge tailored to special needs of clients with injuries, disabilities and chronic health conditions. We pride ourselves on upholding that reputation and exceeding the expectations of referrers and clients with a less ordinary level of specialised care. From CSAS participants with severe disabilities to RIA claimants recovering from life-altering accidents, our highly trained, human-centred physiotherapists, chiropractors, occupational therapists, psychologists and dietitians meet each client where they are and support them to live rich, satisfying lives.</p>
        <h3>Tidewell Care and the CSAS</h3>
      </div>
    </div>
    <div class="brand-mark">Tidewell Care</div>
    <div class="folio">4</div>
    <div class="bands"><span class="b1"></span><span class="b2"></span><span class="b3"></span><span class="b4"></span><span class="b5"></span><span class="b6"></span></div>
  </section>

  <section class="page page--right">
    <svg class="guides" viewBox="0 0 540 797" aria-hidden="true">
      <g stroke="rgba(120,130,140,.18)" stroke-width="1" fill="none">
        <line x1="0" y1="60" x2="300" y2="797"/>
        <line x1="540" y1="40" x2="120" y2="420"/>
        <line x1="200" y1="0" x2="540" y2="620"/>
      </g>
    </svg>
    <h2 class="page-title">ACCEPTED SCHEMES AND PROGRAMS</h2>
    <div class="scheme-name">CSAS</div>
    <div class="columns">
      <div class="col">
        <p>If you’re living with a disability, you’re probably familiar with the challenges of accessing the help you need. Not only can the required frequency of therapy make paying fees unaffordable, funding provisions and onerous application processes can further delay treatment. At Tidewell Care, we recognise the importance of accessing the therapeutic services you need, when you need them. As a registered CSAS provider, Tidewell Care’s practitioners treat eligible participants under the Community Support Access Scheme (CSAS). What’s more, our community coordinator and customer service team are well-versed in CSAS requirements and can help you to fast-track access to appropriate treatment.</p>
        <h3>CSAS services</h3>
        <p>As a registered CSAS provider, Tidewell Care provides our services to all local participants under the CSAS. Ways in which our therapists can help eligible participants to live well and thrive include:</p>
        <h3>Realise your physical goals with your Tidewell Care physiotherapist</h3>
        <p>Whether you’re determined to achieve a certain functional goal, or look forward to relief from pain, swelling or stiffness, our experienced therapists can help. As well as using hands-on techniques, a Tidewell Care physiotherapist may plan a tailored exercise program and even hydrotherapy to help you reach your functional goals. Our physios can also help you with assistive technology, gait rehabilitation, neurological rehabilitation and postural devices.</p>
        <h3>Harness the healing power of food with your Tidewell Care dietitian</h3>
        <p>When it comes to realising your physical and mental potential, food is rarely given due credit. Not only can obtaining optimal quantities and combinations of nutrients assist with the body’s own repair processes, following tailored healthy eating recommendations from a Tidewell Care dietitian can restore a sense of vitality you may have thought you’d lost.</p>
        <h3>Learn what it means to ‘live your best life’ with your Tidewell Care occupational therapist</h3>
        <p>With the right assistance, you may be surprised by how rich and fulfilling your life can be. From recommending rails and aids to advising on assistive technologies, your therapist helps you say the words, ‘I can’.</p>
      </div>
      <div class="col">
        <h3>Feel the power of physical fitness and strength with yoga and Pilates</h3>
        <p>It may sound unlikely that small gains to flexibility, balance and coordination could lead a sense of empowerment and overall strength, but those who have experienced Pilates and yoga attest to the unique benefits of these physical practices. Whether you have your yoga or Pilates technique down pat or need one-on-one guidance, Tidewell Care has a suitable program.</p>
        <h3>Maintain independent living with Tidewell Care domestic assistance and garden maintenance</h3>
        <p>Even if you are able to manage cleaning the house and other domestic tasks, the effort and time required to complete daily chores may leave you too tired to enjoy a rich and full life doing what you want to do. That’s why we offer domestic assistance. Why not relieve some of the burden and let us help with tasks such as daily chores, cleaning and even grocery shopping?</p>
        <h3>Embrace the joy of sharing with Tidewell Care’s regular physical, recreational and social events</h3>
        <p>It can be hard to maintain social ties and activities when your mobility is limited – and sometimes you simply mightn’t feel like making small talk. But the mental health benefits of social interaction are backed by a host of evidence. Let us know if you’re interested and we’ll let you know when we are planning a social event.</p>
        <p>Motor vehicle injuries can vary in severity from minor to life-changing. At Tidewell Care, we strive to resolve all injuries caused by transport accidents and collisions. The services available to RIA clients have been selected and tailored to address the physical, mental and emotional effects of injuries caused by road trauma. Our services are designed to relieve the financial burden of your accident and ensure that you receive the treatment you need, when you need it, without out-of-pocket fees. You can access our services through the RIA as soon as you have a claim number, without a referral, meaning you can dedicate your full focus to making an efficient and satisfying recovery.</p>
      </div>
    </div>
    <div class="folio">5</div>
    <div class="bands"><span class="b1"></span><span class="b2"></span><span class="b3"></span><span class="b4"></span><span class="b5"></span><span class="b6"></span></div>
  </section>
</div>
</body>
</html>
```